Improve My Resume Design to be easier for the reader and the recruiter

I need to improve my resume design to make it easier to read and attract employer eyes in a very professional way. And the graphs should be neat, nice and professional. - You can use the below logos as the companies that I worked with are so famous.

Detailed information about me is inside the CV.

Target Market(s)

Big Companies and Famous recruiters

Industry/Entity Type

Government

Colors

Designer to choose colors to be used in the design.

Requirements
Must have
• Infographics .. Easy to Read.
Nice to have
• Charts, infographics.
Should not have
• not professional colours.

```html
<!DOCTYPE html>
<html lang="en">
<head>
<meta charset="utf-8">
<title>Resume – Karim Nabil Hassan Odeh</title>
<link rel="stylesheet" href="https://fonts.googleapis.com/css2?family=Archivo:wght@300;400;700;800&family=Arimo:ital,wght@0,400;0,700;1,400&family=Open+Sans:ital@1&display=swap">
<style>
:root{
  --page-bg:#d9d9db;
  --frame-grey:#bdbdc0;
  --panel:#e7e7e9;
  --ink:#111111;
  --black:#050505;
  --white:#ffffff;
  --soft-white:#e9e9e9;
}
*{margin:0;padding:0;box-sizing:border-box}
html,body{width:1180px;height:1200px;overflow:hidden;background:var(--page-bg)}
.resume{
  position:absolute;left:178px;top:10px;width:785px;height:1125px;
  transform:scale(1.05);transform-origin:0 0;
  background:var(--frame-grey);overflow:hidden;
  font-family:'Arimo',Arial,sans-serif;color:var(--ink);
}
.frame-shape{position:absolute;left:0;top:0}
.panel{position:absolute;left:32px;top:32px;width:723px;height:908px;background:var(--panel)}
.abs{position:absolute}
.name-first{left:62px;top:74px;font-family:'Archivo',sans-serif;font-weight:400;font-size:37px;letter-spacing:.5px;line-height:1}
.name-last{left:61px;top:114px;font-family:'Archivo',sans-serif;font-weight:800;font-size:37px;letter-spacing:.6px;line-height:1}
.personal{right:57px;top:76px;text-align:right;font-family:'Archivo',sans-serif;font-size:12.5px;line-height:19px;letter-spacing:.8px}
.personal b{font-weight:700}
.contact-bar{left:62px;top:157px;width:668px;height:35px;background:var(--black);color:var(--white);
  font-family:'Archivo',sans-serif;font-weight:700;font-size:20.5px;line-height:35px;text-align:center;letter-spacing:.6px}
.section-title{font-family:'Archivo',sans-serif;font-weight:800;font-size:18px;letter-spacing:2px;line-height:22px}
.rule{position:absolute;width:2px;background:var(--ink)}
.entries{font-size:11px;line-height:13.6px}
.entries p{margin-bottom:13.6px}
.entries p:last-child{margin-bottom:0}
.assignment{left:415px;top:865px;width:297px;height:35px;background:var(--black);color:var(--white);
  font-family:'Open Sans',sans-serif;font-style:italic;font-size:11px;line-height:14.5px;padding:3px 0 0 15px}
.competencies-title{left:55px;top:957px;color:var(--white);font-family:'Archivo',sans-serif;font-weight:700;font-size:19px;letter-spacing:2.4px}
.competencies{list-style:none;color:var(--soft-white);font-size:11px;line-height:24.2px}
.competencies li::before{content:"•";margin-right:6px}
</style>
</head>
<body>
<main class="resume">
  <svg class="frame-shape" width="785" height="1125" viewBox="0 0 785 1125" aria-hidden="true">
    <polygon points="0,746 785,486 785,1125 0,1125" fill="#050505"/>
  </svg>
  <div class="panel"></div>

  <h1>
    <span class="abs name-first">KARIM</span>
    <span class="abs name-last">NABIL HASSAN ODEH</span>
  </h1>
  <div class="abs personal">
    <div><b>Nationality:</b> Jordanian</div>
    <div><b>Date of Birth:</b> 12th Mar 1985</div>
    <div><b>Marital Status:</b> Married</div>
    <div><b>Languages:</b> English and Arabic</div>
  </div>
  <div class="abs contact-bar">Dubai, UAE | +971 500001234 | k.odeh85@mailbox.com</div>

  <h2 class="abs section-title" style="left:81px;top:230px">EDUCATION</h2>
  <span class="rule" style="left:81px;top:266px;height:82px"></span>
  <div class="abs entries" style="left:101px;top:266px;width:240px">
    <p>Master's Degree in Information Technology Management, Coastal University Dubai, UAE (2010)</p>
    <p>B Sc. (Computer Science), Karak Highlands University Jordan (2006)</p>
  </div>

  <h2 class="abs section-title" style="left:80px;top:376px">PROFESSIONAL<br>DEVELOPMENT</h2>
  <span class="rule" style="left:82px;top:437px;height:300px"></span>
  <div class="abs entries" style="left:100px;top:436px;width:240px">
    <p>Nexora Certified Professional (NCP) in Developing Nexora NexWeb Web Applications Using Nexora Studio</p>
    <p>Certified Business Analysis Practitioner (CBAX) Certificate</p>
    <p>Nexora EPM 2010 Portfolio Management and Business Analysts Training</p>
    <p>Orvel CRM 8.0 Essentials Ed1 Certificate from Orvel Academy<br><i>(20 Sep 2011 - 28th Sep 2011)</i></p>
    <p>Orvel Database Course</p>
    <p>IT - Web Development Training</p>
    <p>Introduction to Nexora Basic Programming</p>
    <p>Many Oil &amp; Gas Conferences and Seminars in Malaysia and Iraq</p>
  </div>

  <h2 class="abs section-title" style="left:79px;top:764px">PROFESSIONAL<br>EXPERIENCE</h2>
  <span class="rule" style="left:82px;top:823px;height:80px"></span>
  <div class="abs entries" style="left:102px;top:822px;width:240px">
    <p>National Bureau for Public Workforce (NBPW) Dubai, UAE (Mar 2017 – Present)</p>
    <p><b>Senior Consultant</b> - Human Resources Systems (Project Management Office)</p>
  </div>

  <h2 class="abs section-title" style="left:413px;top:230px">PROFILE SUMMARY</h2>
  <span class="rule" style="left:415px;top:266px;height:530px"></span>
  <div class="abs entries" style="left:428px;top:266px;width:292px">
    <p>Hands-on exposure in handling all phases of Project Cycle, right from requirement analysis, project scoping, planning &amp; scheduling to the implementation of robust technology solutions within time, budget and quality.</p>
    <p>Proven ability to analyze requirements and the associated systems/applications to further translate business requirements into functional requirements</p>
    <p>Visionary leader, noted for sound, practical management style, and ability to lead high-performing technical and non-technical teams in various departments. Strong track record of developing top talent.</p>
    <p>Extensive experience serving as a liaison between business users and technical team to elicit, analyze, communicate, and validate requirements to understand business problems and opportunities in the context of requirements and recommend solutions that enable the organization to achieve its goals.</p>
    <p>Expert in furnishing business insights and analytics used to advance opportunity identification, process re-engineering and facilitate corporate growth.</p>
    <p>Strong analytical and problem-solving skills coupled with thoroughness and attention to detail</p>
    <p>Skilled collaborator comfortable working across key functional business areas to deploy analytical insights around different functions.</p>
    <p>Adaptability of working independently as well as within cross-functional teams sharing common goals and objectives.</p>
    <p>Exceptional problem solver, with a logical, analytical and creative approach to problem-solving and a meticulous and organized approach to work.</p>
  </div>

  <h2 class="abs section-title" style="left:416px;top:830px">PREVIOUS ASSIGNMENT</h2>
  <div class="abs assignment">Web Developer, Veltrix Integrated Solutions Company<br>Amman, Jordan (Jul 2006 - Jun 2007)</div>

  <h2 class="abs competencies-title">CORE COMPETENCIES</h2>
  <ul class="abs competencies" style="left:55px;top:1005px">
    <li>Leadership &amp; Team Building</li>
    <li>Business/IT Analysis</li>
    <li>Requirements Gathering/Analysis</li>
    <li>Business Consulting</li>
  </ul>
  <ul class="abs competencies" style="left:309px;top:1005px">
    <li>Project Management</li>
    <li>Issues And Crisis Management</li>
    <li>Business Process Re-engineering</li>
    <li>System/Services Support</li>
  </ul>
  <ul class="abs competencies" style="left:565px;top:1005px">
    <li>Client / Stakeholder Management</li>
    <li>Event Management</li>
    <li>Reporting &amp; Documentation</li>
    <li>Business Process Mapping</li>
  </ul>
</main>
</body>
</html>
```